Executive search firm in fashion, luxury and retail industry needs logo and card design.

We are a start-up recruiting firm that specializes in the retail and fashion industry, based in New York. We are looking for something that will appeal to CEO level clients and candidates, but that has a little design edge...not overly corporate but still CEO-appropriate. We have clean, sophisticated taste and want a contemporary feel. Happy to have a two sided card. Not afraid of a little color but it should be high-design, not gimmicky and tasteful.

Quillmart Market(s)

CEO's, HR Leaders, in retail, fashion (i.e. Halvorsen, Quillmart, Otto Brevik)

Industry/Entity Type

Professional Service

Contact Information for Business Card

Calloway Ridge Search Partners
Address to be determined
Larkfield, ST 00481

Marta Velard
Managing Director
(555)038-4172
mvelard@callowayridgesearch.example

Font styles to use
Serif
Sans Serif

Requirements
Must have
• clean lines, crisp graphics, some color. Prefer a graphic treatment over a "logo" per se. No pictures, etc.
Nice to have
• double sided design.
Should not have
• Gimmicks, smaltz, goop. Think Gallery of Current Works, not the Dunmore Holdings. No earth tones, as in beige and brown, no pastels. Strong colors are fine in moderation. Grays are good. Jewel tones are good. No red.

```html
<!DOCTYPE html>
<html lang="en">
<head>
<meta charset="utf-8">
<title>Calloway Ridge Search Partners — Business Card</title>
<link rel="stylesheet" href="https://fonts.googleapis.com/css2?family=Open+Sans:wght@400;600;700&display=swap">
<style>
  :root {
    --stage: #e9e9e7;
    --card-yellow: #efc82e;
    --card-white: #fbfbfb;
    --brand-grey: #858585;
    --rule-grey: #8e8e8e;
    --ink-white: #ffffff;
    --card-shadow: 0 10px 28px rgba(0, 0, 0, 0.18);
  }
  * { box-sizing: border-box; margin: 0; padding: 0; }
  html, body {
    width: 1200px;
    height: 900px;
    overflow: hidden;
    background: var(--stage);
    font-family: "Open Sans", Arial, sans-serif;
  }
  .canvas {
    position: relative;
    width: 1200px;
    height: 900px;
  }
  .card {
    position: absolute;
    width: 520px;
    height: 297px;
    overflow: hidden;
    box-shadow: var(--card-shadow);
  }

  /* Back side */
  .card--back {
    left: 50px;
    top: 240px;
    background: var(--card-yellow);
  }
  .card--back .brand {
    position: absolute;
    right: 34px;
    top: 172px;
    display: flex;
    align-items: center;
    gap: 12px;
  }
  .card--back .brand-mark {
    width: 14px;
    height: 14px;
    border-radius: 50%;
    background: var(--ink-white);
  }
  .card--back .brand-name {
    color: var(--ink-white);
    font-weight: 600;
    font-size: 19px;
    letter-spacing: 0.02em;
  }

  /* Front side */
  .card--front {
    left: 630px;
    top: 360px;
    background: var(--card-white);
  }
  .front-top {
    position: absolute;
    left: 0; top: 0;
    width: 100%;
    height: 150px;
    background: linear-gradient(180deg, #ffffff 0%, #f3f3f3 100%);
  }
  .front-rule {
    position: absolute;
    left: 0; top: 150px;
    width: 100%;
    height: 6px;
    background: var(--rule-grey);
  }
  .front-bottom {
    position: absolute;
    left: 0; top: 163px;
    width: 100%;
    height: 134px;
    background: var(--card-yellow);
  }
  .front-brand {
    position: absolute;
    left: 44px;
    top: 52px;
    display: flex;
    align-items: center;
  }
  .front-brand .brand-mark {
    width: 30px;
    height: 30px;
    background: var(--card-yellow);
  }
  .front-brand .brand-divider {
    width: 1px;
    height: 52px;
    margin: 0 18px;
    background: #cfcfcf;
  }
  .front-brand .brand-name {
    color: var(--brand-grey);
    font-weight: 600;
    font-size: 21px;
    line-height: 1.15;
    letter-spacing: 0.02em;
    width: 260px;
  }

  .contact-lines {
    position: absolute;
    right: 210px;
    top: 198px;
    text-align: right;
    color: var(--ink-white);
    font-size: 13px;
  }
  .contact-line {
    display: flex;
    justify-content: flex-end;
    align-items: center;
    gap: 9px;
    height: 24px;
    white-space: nowrap;
  }
  .contact-line svg { width: 12px; height: 12px; flex: none; }

  .person {
    position: absolute;
    left: 330px;
    top: 178px;
    color: var(--ink-white);
    white-space: nowrap;
  }
  .person-name {
    font-weight: 700;
    font-size: 15px;
    line-height: 1.2;
  }
  .person-title {
    font-size: 12px;
    line-height: 1.4;
  }
  .person-address {
    margin-top: 16px;
    font-size: 13px;
  }
</style>
</head>
<body>
<main class="canvas">

  <section class="card card--back" aria-label="Card back">
    <div class="brand">
      <span class="brand-mark"></span>
      <span class="brand-name">Calloway Ridge Search Partners</span>
    </div>
  </section>

  <section class="card card--front" aria-label="Card front">
    <div class="front-top"></div>
    <div class="front-rule"></div>
    <div class="front-bottom"></div>

    <div class="front-brand">
      <span class="brand-mark"></span>
      <span class="brand-divider"></span>
      <span class="brand-name">Calloway Ridge<br>Search Partners</span>
    </div>

    <div class="contact-lines">
      <div class="contact-line">
        <span>(555)038-4172</span>
        <svg viewBox="0 0 24 24" aria-hidden="true">
          <path fill="#ffffff" d="M6.6 10.8c1.4 2.8 3.8 5.1 6.6 6.6l2.2-2.2c.3-.3.7-.4 1-.2 1.1.4 2.3.6 3.6.6.6 0 1 .4 1 1V20c0 .6-.4 1-1 1C10.6 21 3 13.4 3 4c0-.6.4-1 1-1h3.5c.6 0 1 .4 1 1 0 1.3.2 2.5.6 3.6.1.3 0 .7-.2 1L6.6 10.8z"/>
        </svg>
      </div>
      <div class="contact-line">
        <span>mvelard@callowayridgesearch.example</span>
        <svg viewBox="0 0 24 24" aria-hidden="true">
          <rect x="2" y="5" width="20" height="14" rx="1.5" fill="#ffffff"/>
          <polyline points="3,6 12,13 21,6" fill="none" stroke="#efc82e" stroke-width="2"/>
        </svg>
      </div>
    </div>

    <div class="person">
      <div class="person-name">Marta Velard</div>
      <div class="person-title">Managing Director</div>
      <div class="person-address">Larkfield, ST 00481</div>
    </div>
  </section>

</main>
</body>
</html>
```